KALMIRA PPS / APS - Flyer und Rollup

Wir benötigten für eine Messe einen Flyer und einen Rollup, die auf unser Produktionsplanungssystem (PPS) hinweisen.
Rollup: 85x200cm
Flyer A5: 148 × 210 mm + 3 mm Beschnitt pro Seite = 154 × 216 mm pro Seite

Als Beilage haben wir unser Logo, sowie eine einfache Variante vom Rollup und Flyer mit den gewünschten Inhalten.

Target Market(s)

Produktionsbetriebe

Font styles to use
Other font styles liked:
• Roboto

```html
<!DOCTYPE html>
<html lang="de">
<head>
<meta charset="utf-8">
<title>KALMIRA PPS &amp; APS – Flyer und Rollup</title>
<link href="https://fonts.googleapis.com/css2?family=Roboto:wght@300;400;500;700&display=swap" rel="stylesheet">
<style>
  :root{
    --navy:#1f2365;
    --teal:#3fd7c6;
    --teal-soft:#bfeee8;
    --text:#3e4150;
    --muted:#5b5e6b;
    --paper:#ffffff;
    --bg-top:#e6e6e6;
    --bg-bottom:#c3c3c3;
    --band:#f3f4f8;
  }
  *{box-sizing:border-box;margin:0;padding:0}
  html,body{width:1200px;height:3991px;overflow:hidden}
  body{font-family:'Roboto',sans-serif;color:var(--text);position:relative;background:var(--bg-bottom)}
  .stage-top{position:absolute;left:0;top:0;width:1200px;height:2248px;background:var(--bg-top)}
  .sheet{position:absolute;background:var(--paper);box-shadow:0 2px 6px rgba(0,0,0,.22);overflow:hidden}
  .abs{position:absolute}
  svg.abs{display:block}
  .teal{color:var(--teal)}
  .navy{color:var(--navy)}

  /* flyer front */
  .flyer-front{left:265px;top:104px;width:687px;height:969px}
  .brand-mark{background:var(--teal)}
  .brand-name{font-weight:500;color:#fff;letter-spacing:1px}
  .brand-sub{font-weight:500;color:#fff}
  .headline{color:#fff;font-weight:700}
  .lead-white{color:#fff}
  .claim{font-weight:700;color:var(--navy);font-size:25px}
  .claim .teal{font-weight:500}
  .body-copy{font-size:17.5px;line-height:22px;color:var(--muted)}
  .feature-title{font-size:22px;font-weight:700;color:var(--navy);line-height:26px}
  .footer-rule{left:0;top:916px;width:687px;height:1px;background:#e3e4ea}
  .footer-url{left:0;width:687px;top:932px;text-align:center;font-size:20px;font-weight:700;color:var(--navy)}

  /* flyer back */
  .flyer-back{left:265px;top:1136px;width:687px;height:969px}
  .section-title{left:31px;top:33px;font-size:24px;font-weight:700;color:var(--navy)}
  .section-rule{left:31px;top:73px;width:614px;height:2px;background:var(--teal)}
  .col-title{font-size:17px;font-weight:700;color:var(--navy);line-height:19px}
  .col-rule{width:46px;height:2px;background:var(--teal)}
  .bullets{font-size:14.5px;line-height:18.6px;color:var(--muted);list-style:none}
  .bullets li{padding-left:9px;text-indent:-9px}
  .bullets li::before{content:"• ";font-size:11px}
  .benefit-box{border:2px solid var(--teal-soft);border-radius:4px;background:#fbfcfe}
  .benefit-title{font-size:17px;font-weight:700;color:var(--navy)}
  .check-list{list-style:none;color:var(--navy)}
  .check-list li::before{content:"√ ";color:var(--teal);font-weight:700}
  .partner-badge{background:#fff;border-radius:4px;box-shadow:0 1px 4px rgba(0,0,0,.18)}
  .partner-badge span{position:absolute;left:30%;top:40%;width:40%;height:20%;border-radius:3px;background:#e2e4ea}
  .tagline{font-size:16px;line-height:21px;color:var(--navy)}
  .contact-band{left:0;top:892px;width:687px;height:77px;background:var(--band)}
  .cta{font-size:21px;font-weight:500;color:var(--teal)}
  .contact{font-size:16px;font-weight:500;color:var(--navy)}
  .contact .sep{color:#b8bccb}
  .band-url{color:#fff;font-weight:700;font-size:20px;text-align:center}

  /* rollup */
  .rollup{left:313px;top:2381px;width:619px;height:1455px}
  .hex-label{font-size:26px;line-height:32px;font-weight:500;color:var(--navy);text-align:center;width:180px}
</style>
</head>
<body>
<div class="stage-top"></div>

<!-- FLYER FRONT -->
<section class="sheet flyer-front" aria-label="Flyer Vorderseite">
  <svg class="abs" style="left:0;top:0" width="687" height="480" viewBox="0 0 687 480">
    <polygon points="0,0 687,0 687,101 76,477 0,435" fill="var(--navy)"/>
  </svg>
  <div class="abs brand-mark" style="left:42px;top:47px;width:46px;height:46px"></div>
  <div class="abs brand-name" style="left:104px;top:40px;font-size:40px;line-height:44px">KALMIRA</div>
  <div class="abs brand-sub" style="left:104px;top:86px;font-size:14px">PPS &amp; APS</div>

  <h1 class="abs headline" style="left:42px;top:170px;font-size:33px;line-height:39px">Produktionsplanung,<br>die <span class="teal">mitdenkt.</span></h1>
  <p class="abs lead-white" style="left:42px;top:262px;font-size:17.5px;line-height:21.5px">Die KI-gestützte<br>APS/PPS-Lösung für<br>projektspezifische Fertigung.</p>

  <svg class="abs" style="left:360px;top:80px" width="325" height="356" viewBox="0 0 325 356" role="img" aria-label="Foto: Hände halten ein Tablet mit Produktionsdaten vor einer Fabrikszene">
    <defs>
      <linearGradient id="photoFill" x1="0" y1="0" x2="1" y2="1">
        <stop offset="0" stop-color="#9fc3d8"/>
        <stop offset=".55" stop-color="#5f7f9c"/>
        <stop offset="1" stop-color="#d8e2ea"/>
      </linearGradient>
    </defs>
    <polygon points="162,8 312,93 312,263 162,348 12,263 12,93" fill="url(#photoFill)" stroke="var(--teal)" stroke-width="4"/>
  </svg>

  <p class="abs claim" style="left:135px;top:500px"><span class="teal">Automatisch</span>. Transparent. Integriert.</p>
  <p class="abs body-copy" style="left:137px;top:544px">Jeder Auftrag ist anders. KALMIRA plant automatisch, reagiert<br>flexibel und sorgt für volle Transparenz in Ihrer Produktion.</p>

  <svg class="abs" style="left:63px;top:632px" width="40" height="40" viewBox="0 0 40 40">
    <rect x="3" y="3" width="34" height="34" rx="2" fill="none" stroke="var(--teal)" stroke-width="3"/>
    <polyline points="10,27 17,19 22,23 30,13" fill="none" stroke="var(--teal)" stroke-width="3"/>
    <polyline points="24,13 30,13 30,19" fill="none" stroke="var(--teal)" stroke-width="3"/>
  </svg>
  <h2 class="abs feature-title" style="left:135px;top:627px">Intelligent planen</h2>
  <p class="abs body-copy" style="left:135px;top:652px">Unser genetischer Optimierungsalgorithmus findet die beste<br>Reihenfolge — automatisch und in Minuten statt Tagen.</p>

  <svg class="abs" style="left:64px;top:727px" width="40" height="36" viewBox="0 0 40 36">
    <rect x="0" y="18" width="8" height="16" fill="var(--teal)"/>
    <rect x="11" y="12" width="8" height="22" fill="var(--teal)"/>
    <rect x="22" y="20" width="8" height="14" fill="var(--teal)"/>
    <rect x="33" y="4" width="7" height="30" fill="var(--teal)"/>
  </svg>
  <h2 class="abs feature-title" style="left:135px;top:719px">Klar auswerten</h2>
  <p class="abs body-copy" style="left:135px;top:744px">Von der Vorkalkulation bis zur Nachkalkulation.<br>Business-KPIs nach Theory of Constraints inklusive.</p>

  <svg class="abs" style="left:58px;top:812px" width="50" height="48" viewBox="0 0 50 48">
    <g fill="none" stroke="var(--teal)" stroke-width="3">
      <circle cx="25" cy="8" r="5"/><circle cx="8" cy="40" r="5"/><circle cx="42" cy="40" r="5"/><circle cx="25" cy="30" r="4"/>
      <line x1="25" y1="13" x2="25" y2="26"/><line x1="22" y1="33" x2="12" y2="37"/><line x1="28" y1="33" x2="38" y2="37"/>
    </g>
  </svg>
  <h2 class="abs feature-title" style="left:135px;top:811px">Nahtlos integrieren</h2>
  <p class="abs body-copy" style="left:135px;top:836px">Fintrax-Anbindung ab Werk. Für alle anderen Systeme<br>steht eine offene REST-API bereit.</p>

  <div class="abs footer-rule"></div>
  <div class="abs footer-url">kalmira-pps.ch</div>
</section>

<!-- FLYER BACK -->
<section class="sheet flyer-back" aria-label="Flyer Rückseite">
  <h2 class="abs section-title">Alles, was Ihre Produktion braucht — in einem System.</h2>
  <div class="abs section-rule"></div>

  <svg class="abs" style="left:0;top:100px" width="687" height="150" viewBox="0 0 687 150">
    <g fill="#fff" stroke="var(--teal-soft)" stroke-width="2">
      <polygon points="125,5 187,40 187,110 125,145 63,110 63,40"/>
      <polygon points="331,5 393,40 393,110 331,145 269,110 269,40"/>
      <polygon points="545,5 607,40 607,110 545,145 483,110 483,40"/>
    </g>
    <g fill="none" stroke="var(--navy)" stroke-width="2">
      <rect x="116" y="48" width="18" height="10"/><line x1="125" y1="58" x2="125" y2="68"/>
      <line x1="106" y1="68" x2="144" y2="68"/><rect x="98" y="68" width="16" height="12"/><rect x="136" y="68" width="16" height="12"/>
      <line x1="106" y1="80" x2="106" y2="92"/><line x1="144" y1="80" x2="144" y2="92"/>
      <rect x="306" y="50" width="40" height="34"/><rect x="336" y="70" width="24" height="32"/>
      <line x1="340" y1="78" x2="356" y2="78"/><line x1="340" y1="86" x2="356" y2="86"/><line x1="340" y1="94" x2="356" y2="94"/>
      <ellipse cx="535" cy="56" rx="16" ry="6"/><path d="M519 56v36c0 3 7 6 16 6s16-3 16-6V56"/>
      <path d="M519 68c0 3 7 6 16 6s16-3 16-6M519 80c0 3 7 6 16 6s16-3 16-6"/>
      <rect x="552" y="58" width="16" height="22"/><rect x="560" y="66" width="16" height="22"/>
    </g>
    <g fill="var(--teal)">
      <circle cx="106" cy="94" r="4"/><circle cx="144" cy="94" r="4"/><circle cx="326" cy="62" r="7"/>
      <rect x="306" y="88" width="6" height="14"/><rect x="314" y="82" width="6" height="20"/><rect x="322" y="90" width="6" height="12"/>
    </g>
  </svg>

  <h3 class="abs col-title" style="left:57px;top:272px">PLANUNG<br>&amp; STEUERUNG</h3>
  <div class="abs col-rule" style="left:57px;top:319px"></div>
  <ul class="abs bullets" style="left:46px;top:334px;width:200px">
    <li>Automatische<br>&nbsp;&nbsp;Feinplanung (KI)</li>
    <li>Dynamische Umplanung</li>
    <li>Ressourcenoptimierung</li>
    <li>Auftragsfortschritt</li>
    <li>Intuitive Plantafel</li>
  </ul>

  <h3 class="abs col-title" style="left:262px;top:294px">KALKULATION</h3>
  <div class="abs col-rule" style="left:262px;top:321px"></div>
  <ul class="abs bullets" style="left:262px;top:336px;width:200px">
    <li>Vorkalkulation</li>
    <li>Mitlaufende<br>&nbsp;&nbsp;Kalkulation</li>
    <li>Nachkalkulation</li>
    <li>Herstellkosten</li>
    <li>Projektabgrenzung</li>
    <li>Business-KPIs (TOC)</li>
  </ul>

  <h3 class="abs col-title" style="left:481px;top:291px">INTEGRATION</h3>
  <div class="abs col-rule" style="left:481px;top:318px"></div>
  <ul class="abs bullets" style="left:481px;top:333px;width:190px">
    <li>Stücklisten-Pflege</li>
    <li>Arbeitspläne</li>
    <li>Fintrax-Integration</li>
    <li>REST-API</li>
    <li>BDE-Rückmeldungen</li>
  </ul>

  <div class="abs benefit-box" style="left:34px;top:500px;width:613px;height:166px"></div>
  <h3 class="abs benefit-title" style="left:172px;top:524px">Ihr Nutzen im Überblick</h3>
  <ul class="abs check-list" style="left:153px;top:563px;font-size:17px;line-height:26.5px">
    <li>Bis zu 50% weniger Planungsaufwand</li>
    <li>Höhere Termintreue durch KI-Optimierung</li>
    <li>Planung immer aktuell — auch bei Störungen</li>
  </ul>

  <div class="abs partner-badge" style="left:31px;top:734px;width:145px;height:65px"><span></span></div>
  <div class="abs partner-badge" style="left:186px;top:734px;width:145px;height:65px"><span></span></div>
  <div class="abs partner-badge" style="left:341px;top:734px;width:145px;height:65px"><span></span></div>
  <div class="abs partner-badge" style="left:496px;top:734px;width:145px;height:65px"><span></span></div>

  <p class="abs tagline" style="left:31px;top:826px">Schweizer APS/PPS-Lösung, entwickelt von<br>Produktionsprofis für Produktionsprofis.</p>

  <div class="abs contact-band"></div>
  <svg class="abs" style="left:0;top:842px" width="687" height="127" viewBox="0 0 687 127">
    <polygon points="498,0 687,0 687,127 463,127" fill="var(--teal)"/>
    <polygon points="478,74 687,74 687,127 463,127" fill="var(--navy)"/>
  </svg>
  <div class="abs cta" style="left:31px;top:900px">Demo vereinbaren</div>
  <div class="abs contact" style="left:31px;top:930px">info@kalmira-pps.ch <span class="sep">|</span> +41 00 000 00 00</div>
  <div class="abs band-url" style="left:480px;top:928px;width:207px">kalmira-pps.ch</div>
</section>

<!-- ROLLUP -->
<section class="sheet rollup" aria-label="Rollup">
  <svg class="abs" style="left:0;top:0" width="619" height="640" viewBox="0 0 619 640">
    <polygon points="0,0 619,0 619,365 147,635 0,550" fill="var(--navy)"/>
  </svg>
  <div class="abs brand-mark" style="left:56px;top:52px;width:96px;height:96px"></div>
  <div class="abs brand-name" style="left:183px;top:50px;font-size:66px;line-height:70px">KALMIRA</div>
  <div class="abs brand-sub" style="left:184px;top:120px;font-size:22px">PPS &amp; APS</div>

  <h1 class="abs headline" style="left:53px;top:224px;font-size:45px;line-height:57px">Produktionsplanung,<br>die <span class="teal">mitdenkt.</span></h1>
  <p class="abs lead-white" style="left:51px;top:372px;font-size:30px;line-height:37px;font-weight:300">KI-gestützte<br>APS/PPS-Lösung</p>

  <svg class="abs" style="left:0;top:690px" width="619" height="145" viewBox="0 0 619 145">
    <g fill="#fff" stroke="var(--teal-soft)" stroke-width="2">
      <polygon points="115,4 175,38 175,106 115,140 55,106 55,38"/>
      <polygon points="310,4 370,38 370,106 310,140 250,106 250,38"/>
      <polygon points="506,4 566,38 566,106 506,140 446,106 446,38"/>
    </g>
    <g fill="none" stroke="var(--navy)" stroke-width="2">
      <rect x="106" y="46" width="18" height="10"/><line x1="115" y1="56" x2="115" y2="66"/>
      <line x1="96" y1="66" x2="134" y2="66"/><rect x="88" y="66" width="16" height="12"/><rect x="126" y="66" width="16" height="12"/>
      <line x1="96" y1="78" x2="96" y2="90"/><line x1="134" y1="78" x2="134" y2="90"/>
      <rect x="285" y="48" width="40" height="34"/><rect x="315" y="68" width="24" height="32"/>
      <line x1="319" y1="76" x2="335" y2="76"/><line x1="319" y1="84" x2="335" y2="84"/><line x1="319" y1="92" x2="335" y2="92"/>
      <ellipse cx="496" cy="54" rx="16" ry="6"/><path d="M480 54v36c0 3 7 6 16 6s16-3 16-6V54"/>
      <path d="M480 66c0 3 7 6 16 6s16-3 16-6M480 78c0 3 7 6 16 6s16-3 16-6"/>
      <rect x="513" y="56" width="16" height="22"/><rect x="521" y="64" width="16" height="22"/>
    </g>
    <g fill="var(--teal)">
      <circle cx="96" cy="92" r="4"/><circle cx="134" cy="92" r="4"/><circle cx="305" cy="60" r="7"/>
      <rect x="285" y="86" width="6" height="14"/><rect x="293" y="80" width="6" height="20"/><rect x="301" y="88" width="6" height="12"/>
    </g>
  </svg>
  <div class="abs hex-label" style="left:25px;top:866px">Intelligent<br>planen</div>
  <div class="abs hex-label" style="left:220px;top:863px">Klar<br>auswerten</div>
  <div class="abs hex-label" style="left:416px;top:860px">Nahtlos<br>integrieren</div>

  <div class="abs benefit-box" style="left:42px;top:986px;width:537px;height:138px"></div>
  <ul class="abs check-list" style="left:71px;top:1021px;font-size:26px;line-height:37px;font-weight:500">
    <li>Bis zu 50% weniger Planungsaufwand</li>
    <li>Höhere Termintreue</li>
  </ul>

  <ul class="abs check-list" style="left:71px;top:1174px;font-size:26px;line-height:37px;font-weight:500">
    <li>Automatische Planung</li>
    <li>Echtzeit-Transparenz</li>
    <li>REST-API</li>
    <li>Fintrax Integration</li>
  </ul>

  <svg class="abs" style="left:0;top:1322px" width="619" height="133" viewBox="0 0 619 133">
    <rect x="0" y="46" width="619" height="87" fill="var(--navy)"/>
    <polygon points="455,0 619,0 619,133 389,133" fill="var(--teal)"/>
  </svg>
  <div class="abs cta" style="left:53px;top:1390px;font-size:31px;font-weight:700">Demo vereinbaren</div>
  <div class="abs" style="left:420px;top:1410px;width:190px;text-align:center;font-size:21px;font-weight:500;color:var(--navy)">kalmira-pps.ch</div>
</section>
</body>
</html>
```